Website Design Front page Holistic Members site & Natural Therapist Directory

I need a modern, fresh unique look for a natural therapy and holistic/ Spiritual directory & educational website. It needs to be clear, colourful, inviting and suitable for both sexes - young and old. I want it look fresh and super modern.

I will require the design in .psd format and anything in the centre section including rotational image needs to be supplied in .ai so I can break down the components and colours used will also be needed for frames and banners.

Target Market(s)

all ages, male and female. It must appeal to both therapists and general public.

Requirements
Must have
• Logo obviously. Room for a video player 300 x 250. And small introduction text panel. Must follow the layout in file attached. Also a rotating image up the top, in main section (have supplied example image alter as you like - man pointing top right). Have also supplied example of text to have on it. 16 Menu bars on left frame, under home. Must have 6 prominent links to main pages of site. Have included images use if you want or else use your own. These 6 are, Find a Psychic/ Medium, Find a Natural Therapist, Find a Business/ Club/ School, Find an Event/ Workshop, Find a Product, Holistic Career Centre.I have also attached a shot of the emag, although nothing special in design, useful for complimentary colour choices but not limited to. Another link image/ banner would be Free Chat Now.Another if room and not over crowded would be compare memberships. Can use leader board and leader ad board. Also require the footer to be designed and delivered in .ai similar to craft pebble with link image to chatterly and blurbo.
Nice to have
• Compare memberships link would be great but not essential... don't want page to look too busy.
Should not have
• Must not be too busy.. think zen with a modern twist.

```html
<!DOCTYPE html>
<html lang="en">
<head>
<meta charset="utf-8">
<title>Soul Chorus – Holistic Community</title>
<link href="https://fonts.googleapis.com/css2?family=Arimo:wght@400;700&display=swap" rel="stylesheet">
<style>
:root{
  --ink:#333;
  --muted:#555;
  --blue:#2f6db5;
  --blue-dark:#1d4f8f;
  --sky:#5b9bd8;
  --heading:#3b68a8;
  --green:#7cbd3c;
  --green-pale:#e8f2d6;
  --green-pale2:#f1f7e6;
  --orange:#f39a26;
  --orange-pale:#fbc77c;
  --teal:#2aa3b5;
  --panel:#ffffff;
  --footer:#254a84;
  --footer-deep:#16325e;
  --rule:#d8dde4;
}
*{margin:0;padding:0;box-sizing:border-box}
html,body{width:879px;height:1200px;overflow:hidden}
body{font-family:"Arimo",Arial,sans-serif;color:var(--ink);background:#fff}
.page{position:relative;width:879px;height:1200px;overflow:hidden;
  background:linear-gradient(#fff 0,#fff 118px,#2f6aaf 118px,#4f8cd0 122px,#6aa3dc 300px,#5b93d2 900px,#3d72b5 1053px)}
.abs{position:absolute}

/* header */
.top-tab{left:640px;top:0;width:160px;height:24px;background:var(--green);border-radius:0 0 6px 6px;
  color:#fff;font-size:10px;display:flex;justify-content:center;align-items:center;gap:6px}
.brand{left:91px;top:34px;display:flex;align-items:center;gap:8px}
.brand-dot{width:30px;height:30px;border-radius:50%;background:#a8489b}
.brand-name{font-size:27px;font-weight:700;color:#222;letter-spacing:-0.5px}
.contact{right:78px;top:53px;text-align:right}
.contact .small{font-size:11px;color:#444}
.contact .phone{font-size:15px;font-weight:700;color:#222}

/* panel */
.panel{left:76px;top:127px;width:726px;height:926px;background:var(--panel);border-radius:10px;
  box-shadow:0 0 6px rgba(0,0,0,.25)}

/* left column */
.search{left:84px;top:139px;width:125px;height:58px;background:linear-gradient(var(--orange-pale),var(--orange));
  border-radius:4px 4px 0 0;padding:5px 6px}
.search h3{font-size:9px;color:#6a3d05;font-weight:700}
.search .field{margin-top:3px;height:14px;background:#fff;border:1px solid #c77a13;width:112px}
.search .go{margin-top:4px;font-size:8px;font-weight:700;color:#333}
.nav{left:84px;top:197px;width:125px;list-style:none}
.nav li{height:20.6px;line-height:20.6px;padding-left:8px;font-size:8px;font-weight:700;color:#333;
  background:var(--green-pale);border-bottom:1px solid #fff}
.nav li:nth-child(even){background:var(--green-pale2)}
.nav li.current{background:var(--green);color:#fff}
.nav li.signin{background:#cfe6f3}
.featured{left:84px;top:547px;width:125px;height:387px;border:1px solid #bcd3ea;background:#f5f8fb}
.box-head{height:22px;background:linear-gradient(#4f8fd0,var(--blue-dark));color:#fff;font-size:9px;font-weight:700;
  line-height:22px;padding-left:8px}
.member-photo{margin:12px auto 0;width:108px;height:82px;border:3px solid #e3e6ea;background:linear-gradient(135deg,#d8dde3,#f3f4f6)}
.member-name{font-size:7.5px;font-weight:700;color:var(--orange);margin:8px 8px 2px}
.member-info{font-size:8px;line-height:11px;color:var(--muted);margin:0 8px}
.btn{display:inline-block;height:16px;line-height:16px;padding:0 10px;border-radius:8px;
  background:linear-gradient(#9bd15b,#5f9e2a);color:#123;font-size:7.5px;font-weight:700;border:1px solid #4f8a22}

/* center */
.hero{left:217px;top:140px;width:422px;height:180px;border-radius:6px 6px 0 0;overflow:hidden;
  background:linear-gradient(#2e8cc8,#7cc0e6 55%,#eaf6fc 80%,#bfe3f2)}
.hero-menu{left:467px;top:155px;width:171px}
.hero-menu div{height:23px;margin-bottom:3.3px;background:linear-gradient(#5aa6d6,#2f7db8);border:1px solid #9fd0ef;
  color:#0d2740;font-size:8.5px;font-weight:700;line-height:21px;padding-left:12px}
.hero-menu div:nth-child(3),.hero-menu div:nth-child(5){background:linear-gradient(#6fb6e0,#3a89c2)}
.hero-menu div:nth-child(6){background:#2f7db8}
.hero-base{left:217px;top:312px;width:422px;height:8px;background:#1f6fa8}
h1.intro-title{left:217px;top:338px;font-size:18px;color:var(--heading);font-weight:700}
.intro{left:217px;top:372px;width:192px;font-size:8.4px;line-height:12px;color:var(--muted)}
.intro p{margin-bottom:12px}
.intro b{color:#333}
.video{left:419px;top:375px;width:220px;height:175px;background:#111}
.video-frame{width:220px;height:158px;background:radial-gradient(circle at 65% 35%,#d9c7a6,#6e5a45 45%,#1c1712 80%)}
.video-bar{height:17px;background:linear-gradient(#f3f3f3,#cfcfcf);display:flex;align-items:center;gap:5px;padding:0 4px;font-size:6px;color:#333}
.video-bar .track{flex:1;height:4px;background:#999;border-radius:2px}
.tiles{left:217px;top:573px;width:422px;display:grid;grid-template-columns:repeat(3,135px);column-gap:8px;row-gap:7px}
.tile{height:110px;border:2px solid;border-radius:6px;overflow:hidden;display:flex;flex-direction:column}
.tile .img{flex:1}
.tile .label{height:26px;line-height:26px;color:#fff;font-size:8.5px;font-weight:700;padding-left:8px}
.t-orange{border-color:var(--orange)} .t-orange .label{background:var(--orange)}
.t-green{border-color:var(--green)} .t-green .label{background:var(--green)}
.t-teal{border-color:var(--teal)} .t-teal .label{background:var(--teal)}
h2.sub-title{left:217px;top:816px;font-size:14.5px;color:var(--orange);font-weight:700}
.body-copy{left:217px;top:840px;width:422px;font-size:8.2px;line-height:12px;color:var(--muted)}

/* right column */
.side{left:647px;width:145px;border:1px solid #bcd3ea;background:#f7f9fb}
.side .box-head{display:flex;align-items:center;gap:6px;padding-left:6px}
.side .ico{width:14px;height:14px;border-radius:3px;background:#fff;opacity:.9}
.profile{top:139px;height:121px}
.profile .box-head{background:linear-gradient(#8a8a8a,#4c4c4c)}
.profile ul{list-style:none;padding:5px 10px}
.profile li{font-size:7.5px;color:#333;line-height:11.6px}
.profile li::before{content:"› ";color:#777}
.events{top:264px;height:123px}
.news{top:390px;height:217px}
.testi{top:611px;height:216px}
.testi .box-head{background:linear-gradient(#3a90d8,#1f63a8)}
.entry{margin:0 8px;padding:6px 0 6px 4px;border-bottom:1px solid var(--rule);font-size:7.5px;line-height:10px;color:#444}
.entry::before{content:"• ";}
.entry span{display:block;padding-left:6px}
.side .more{margin:8px 10px}
.quote{font-size:8px;line-height:12px;color:#333;margin:10px 14px 0}
.quote b{display:block;margin-top:2px}
.subscribe{left:647px;top:834px;width:145px;height:100px;border:1px solid #ddd;background:#fff}
.subscribe h4{font-size:13px;font-weight:700;color:#222;margin:10px 0 0 8px}
.subscribe .sm{font-size:8px;color:#444;margin-left:8px;font-weight:700}
.subscribe .field{margin:6px 8px;height:18px;border:1px solid #ccc;font-size:8px;color:#888;padding:4px}
.subscribe .cta{position:absolute;left:0;bottom:0;width:143px;height:20px;background:var(--orange);color:#fff;
  font-size:11px;font-weight:700;text-align:center;line-height:20px}

/* ad */
.divider{left:84px;top:954px;width:710px;height:1px;background:var(--rule)}
.ad{left:173px;top:970px;width:534px;height:67px;border:1px solid #cbd6e2;display:flex;align-items:center;
  background:linear-gradient(90deg,#3aa6c9,#bfe6ef 25%,#fff 30%)}
.ad .scene{width:95px;height:100%}
.ad .copy{flex:1;text-align:center}
.ad .big{font-size:24px;color:#e68a1c}
.ad .tag{font-size:8px;font-weight:700;color:#2a6f92;letter-spacing:.5px}
.ad .badge{width:60px;height:60px;margin-right:8px;border-radius:50%;background:#e9f2f7}

/* footer */
.footer{left:0;top:1053px;width:879px;height:121px;background:linear-gradient(var(--footer),#203f73)}
.fcol{top:1066px;color:#fff}
.fcol h5{font-size:11px;font-weight:700;margin-bottom:5px}
.fcol ul{list-style:none;padding-left:6px}
.fcol li{font-size:9px;line-height:12.4px}
.fcol li::before{content:"→ ";font-size:8px}
.social{display:flex;flex-direction:column;gap:3px;margin-top:2px}
.social span{font-size:9px;display:flex;align-items:center;gap:5px}
.social i{width:9px;height:9px;background:#4fb1e6;border-radius:2px;display:inline-block}
.copyright{left:0;top:1174px;width:879px;height:26px;background:var(--footer-deep);color:#7fb3e8;font-size:8px;
  text-align:center;line-height:26px}
</style>
</head>
<body>
<div class="page">

  <header>
    <nav class="abs top-tab"><span>Contact Us</span><span>|</span><span>Sign In</span><span>|</span><span>Register</span></nav>
    <div class="abs brand"><span class="brand-dot"></span><span class="brand-name">Soul Chorus</span></div>
    <div class="abs contact"><div class="small">For More Information</div><div class="phone">Call Us: 0123 456 789</div></div>
  </header>

  <div class="abs panel"></div>

  <!-- left column -->
  <form class="abs search">
    <h3>COMMUNITY SEARCH</h3>
    <div class="field"></div>
    <div class="go">Search ▸</div>
  </form>
  <ul class="abs nav">
    <li class="current">HOME</li><li>ABOUT US</li><li>LATEST NEWS</li><li>COMMUNITY CALENDAR</li>
    <li>MEMBER SEARCH</li><li class="signin">SIGN IN</li><li>EXCLUSIVE INTERVIEWS</li><li>GUEST PSYCHIC</li>
    <li>FENG SHUI</li><li>YOGA &amp; MEDITATION</li><li>TAROT</li><li>NUMEROLOGY</li><li>CHAKRAS</li>
    <li>BOOK CLUB</li><li>GIVE AWAYS</li><li>HEALTHY RECIPES</li><li>MEMBER SEARCH</li>
  </ul>
  <aside class="abs featured">
    <div class="box-head">FEATURED MEMBERS</div>
    <div class="member-photo" role="img" aria-label="Portrait of a featured clairvoyant member"></div>
    <div class="member-name">CLAIRVOYANT M</div>
    <div class="member-info">Psychic/ Medium, Reiki Master, Trance Channeler, Author, Workshop Facilitator, connect with Spirit</div>
    <div class="member-photo" role="img" aria-label="Portrait of a featured tarot reader member"></div>
    <div class="member-name">DANA ELISE</div>
    <div class="member-info">Tarot, Numerologist, Reiki Master, Crystal Therapist, Author, Workshop Facilitator, Moonlit Path Tarot</div>
    <div style="margin:12px 0 0 8px"><span class="btn">READ MORE ▸</span></div>
  </aside>

  <!-- center -->
  <div class="abs hero" role="img" aria-label="Man in white sitting cross-legged by the sea, pointing to the top right"></div>
  <div class="abs hero-base"></div>
  <nav class="abs hero-menu">
    <div>FIND A PSYCHIC/ MEDIUM</div><div>FIND A NATURAL THERAPIST</div><div>FIND A BUSINESS/ CLUB/ SCHOOL</div>
    <div>FIND AN EVENT/ WORKSHOP</div><div>FIND A PRODUCT</div><div>HOLISTIC CAREER CENTRE</div>
  </nav>

  <h1 class="abs intro-title">Lorem Ipsum is simply dummy text</h1>
  <div class="abs intro">
    <p>Welcome to <b>Soul Chorus</b> Community &amp; chat rooms. We hope you will explore the various features our sites has to offer. We created this online space for log on and create a dynamic member profile, collaborate on projects, share your ideas and expertise - and, most portant, connect with your fellow members.</p>
    <p>Share, collaborate, exchange and grow - that's why we're here and we hope you are too. Engage and explore anytime, from anywhere there's a web connection.</p>
    <p><b>Share. Learn. Grow.</b></p>
  </div>
  <div class="abs video">
    <div class="video-frame" role="img" aria-label="Video still of a lit candle beside a book and tarot cards">
      <svg width="220" height="158" viewBox="0 0 220 158"><circle cx="110" cy="79" r="16" fill="rgba(255,255,255,.45)"/><path d="M104 70 L120 79 L104 88Z" fill="#fff"/></svg>
    </div>
    <div class="video-bar"><span>▮▮</span><span>◀)</span><span class="track"></span><span>0:00/10:32</span><span>360p</span><span>▭</span><span>⤢</span></div>
  </div>

  <div class="abs tiles">
    <a class="tile t-orange"><div class="img" role="img" aria-label="Candle and tarot cards" style="background:linear-gradient(#2a221b,#8c7458)"></div><div class="label">Find a Psychic</div></a>
    <a class="tile t-green"><div class="img" role="img" aria-label="Woman receiving a head massage" style="background:linear-gradient(#cfe7f2,#e9d6c6)"></div><div class="label">Find a Therapist</div></a>
    <a class="tile t-teal"><div class="img" role="img" aria-label="Warmly lit spa treatment room" style="background:linear-gradient(#b9772c,#e2b45c)"></div><div class="label">Find a Business / School</div></a>
    <a class="tile t-orange"><div class="img" role="img" aria-label="Hand writing with a pen on paper" style="background:linear-gradient(#e7eef6,#b8c9dc)"></div><div class="label">Find an Event/ Workshop</div></a>
    <a class="tile t-green"><div class="img" role="img" aria-label="Flowers and essential oil bottles" style="background:linear-gradient(#f3e9f1,#b8a3b0)"></div><div class="label">Find a Product</div></a>
    <a class="tile t-teal"><div class="img" role="img" aria-label="Jobs sign against a blue sky" style="background:linear-gradient(#1e4f8c,#6fa0d6)"></div><div class="label">Holistic Career Centre</div></a>
  </div>

  <h2 class="abs sub-title">Lorem Ipsum is not simply random text.</h2>
  <p class="abs body-copy">Contrary to popular belief, Lorem Ipsum is not simply random text. It has roots in a piece of classical Latin literature from 45 BC, making it over 2000 years old. Ronald Mercer, a Latin professor at Hollis-Brook College in Virginia, looked up one of the more obscure Latin words, consectetur, from a Lorem Ipsum passage, and going through the cites of the word in classical literature, discovered the undoubtable source. Lorem Ipsum comes from sections 1.10.32 and 1.10.33 of "de Finibus Bonorum et Malorum" (The Extremes of Good and Evil) by Corvinus, written in 45 BC. This book is a treatise on the theory of ethics, very popular during the Renaissance. The first line of Lorem Ipsum, "Lorem ipsum dolor sit amet..", comes from a line in section 1.10.32.</p>

  <!-- right column -->
  <aside class="abs side profile">
    <div class="box-head"><span class="ico"></span>MY PROFILE</div>
    <ul><li>PROFILE HOME</li><li>MANAGE PROFILE</li><li>NETWORKS</li><li>FILES &amp; LINKS</li><li>FAVORITES</li><li>MESSAGES</li><li>CONNECTIONS</li><li>REFER A FRIEND</li></ul>
  </aside>
  <aside class="abs side events">
    <div class="box-head"><span class="ico"></span>EVENTS CALENDAR</div>
    <div class="entry">10/1/2010<span>TECH CONF 2010</span></div>
    <div class="entry">10/8/2010<span>WEB DEV CONF 2010</span></div>
    <div class="more"><span class="btn">READ MORE ▸</span></div>
  </aside>
  <aside class="abs side news">
    <div class="box-head"><span class="ico"></span>LATEST NEWS</div>
    <div class="entry">9/16/2010<span>Lorem ipsum dolor sit amet</span></div>
    <div class="entry">8/26/2010<span>Vestibulum id enim vel</span></div>
    <div class="entry">9/16/2010<span>Integer ac nisi quis felis</span></div>
    <div class="entry">8/26/2010<span>Pellentesque hendrerit velit ac dolor convallis quis lacinia orci iaculis</span></div>
    <div class="more"><span class="btn">READ MORE ▸</span></div>
  </aside>
  <aside class="abs side testi">
    <div class="box-head"><span class="ico"></span>TESTIMONIALS</div>
    <p class="quote">It's like a Spiritual chatterly, where I can make new contacts with similar interests. Top idea...I love it!<b>— Jenna, CA</b></p>
    <p class="quote">I read your latest magazines &amp; I have to tell you I thoughtfully enjoy it. I learnt a lot. I can't wait for next month edition.<b>— Sadie, QLD</b></p>
    <div class="more"><span class="btn">READ MORE ▸</span></div>
  </aside>
  <aside class="abs subscribe">
    <h4>SUBSCRIBE</h4>
    <div class="sm">MONTHLY MAGAZINE</div>
    <div class="field">Your Email Address</div>
    <div class="cta">SUBSCRAIBE NOW!</div>
  </aside>

  <!-- ad -->
  <div class="abs divider"></div>
  <div class="abs ad">
    <div class="scene" role="img" aria-label="Tropical beach with overwater bungalows"></div>
    <div class="copy"><div class="big">share yoga. travel the world.</div><div class="tag">ALL-INCLUSIVE VACATIONS FOR YOGA INSTRUCTORS</div></div>
    <div class="badge"></div>
  </div>

  <!-- footer -->
  <footer>
    <div class="abs footer"></div>
    <div class="abs fcol" style="left:84px"><h5>Find....</h5><ul><li>A Psychic</li><li>A Therapist</li><li>A Business / School</li><li>An Event / Workshop</li><li>A Product</li><li>Holistic Career Center</li></ul></div>
    <div class="abs fcol" style="left:289px"><h5>Popular Pages....</h5><ul><li>Contrary to popular</li><li>Belief Lorem Ipsum</li><li>Is not simply random</li><li>It has roots</li><li>In a piece of classical</li><li>Latin literature</li></ul></div>
    <div class="abs fcol" style="left:488px"><h5>About Soul Chorus....</h5><ul><li>Contrary to popular</li><li>Belief Lorem Ipsum</li><li>Is not simply random</li><li>It has roots</li></ul></div>
    <div class="abs fcol" style="left:648px;top:1093px"><h5>Connect....</h5>
      <div class="social"><span><i></i>snapdot</span><span><i></i>chatterly</span><span><i></i>linkwise</span><span><i></i>blurbo</span><span><i></i>RSS</span></div>
    </div>
    <div class="abs copyright">Copyright 2011 <b>Soul Chorus</b>. All rights reserved</div>
  </footer>

</div>
</body>
</html>
```